Security Company Needs an UPDATED Business Card and Letterhead Design!

I run a security company and would like to have an updated BUSINESS CARD + LETTERHEAD DESIGN.

Please use my UPDATED address below:

2875 E. Thistlewood Drive
Suite 418 Dallas, Texas 75247

Attached is the current business card as reference, and also my logo.

Target Market(s)

High end security users such as Class A buildings, Corporate Campus Locations, Hospitals, High End Retail Centers, Warehousing, Manufacturing and High Tech Companies

Industry/Entity Type

Security Guard

Contact Information for Business Card

Looking for unique, yet professional

Requirements
Must have
• Must use the current logo and incorporate it into any design. Use the colors that are included in the logo. I also need to be able to easily add employees as the company grows. Should be an easy process to change Names and Numbers

```html
<!DOCTYPE html>
<html lang="en">
<head>
<meta charset="utf-8">
<title>Halvorsen Guard Group – Business Card</title>
<link href="https://fonts.googleapis.com/css2?family=Open+Sans:wght@400;600;700&display=swap" rel="stylesheet">
<style>
  :root {
    --backdrop: #3a332f;
    --card: #0d0d0e;
    --card-edge: #1c1c1e;
    --accent-blue: #4ba6e6;
    --text-white: #f2f2f2;
    --brand-silver: #c8ccd3;
    --brand-blue: #4a5fc0;
  }
  * { margin: 0; padding: 0; box-sizing: border-box; }
  html, body {
    width: 1200px; height: 900px; overflow: hidden;
    background: var(--backdrop);
    font-family: "Open Sans", Arial, sans-serif;
  }
  .canvas { position: relative; width: 1200px; height: 900px; }
  .card {
    position: absolute; top: 290px;
    width: 540px; height: 310px;
    background: var(--card);
    border: 1px solid var(--card-edge);
    box-shadow: 0 14px 30px rgba(0,0,0,0.45);
  }
  .card--front { left: 45px; }
  .card--back { left: 615px; }

  .brand {
    position: absolute; display: flex; align-items: center; gap: 10px;
  }
  .brand__dot {
    width: 16px; height: 16px; border-radius: 50%;
    background: var(--brand-blue); flex: none;
  }
  .brand__name {
    font-weight: 700; text-transform: uppercase; letter-spacing: 1px;
    line-height: 1.2;
  }
  .card--front .brand { left: 28px; top: 130px; width: 210px; }
  .card--front .brand__name { color: var(--brand-blue); font-size: 17px; }
  .card--back .brand { left: 0; right: 0; top: 0; bottom: 0; justify-content: center; }
  .card--back .brand__dot { background: var(--brand-silver); width: 20px; height: 20px; }
  .card--back .brand__name { color: var(--brand-silver); font-size: 24px; letter-spacing: 2px; }

  .divider {
    position: absolute; left: 258px; top: 42px; width: 1px; height: 228px;
    background: linear-gradient(var(--accent-blue), rgba(75,166,230,0.15));
  }
  .details { position: absolute; left: 282px; top: 42px; color: var(--text-white); }
  .details__name { color: var(--accent-blue); font-weight: 600; font-size: 19px; line-height: 1.15; }
  .details__title { font-size: 13px; margin-bottom: 20px; }
  .details__address { font-size: 13px; line-height: 1.5; margin-bottom: 16px; }
  .contacts { list-style: none; font-size: 13px; line-height: 1.65; }
  .contacts li { display: flex; align-items: center; gap: 10px; }
  .contacts svg { width: 11px; height: 11px; flex: none; }
</style>
</head>
<body>
<main class="canvas">
  <section class="card card--front">
    <div class="brand">
      <span class="brand__dot"></span>
      <span class="brand__name">Halvorsen Guard Group</span>
    </div>
    <div class="divider"></div>
    <div class="details">
      <p class="details__name">Daniel R. Halvorsen</p>
      <p class="details__title">President &amp; CEO</p>
      <p class="details__address">2875 E. Thistlewood Drive<br>Suite 418 Dallas, Texas 75247</p>
      <ul class="contacts">
        <li><svg viewBox="0 0 12 12"><path d="M2 1l2.5 0 1 3-1.5 1a7 7 0 0 0 3 3l1-1.5 3 1V10a1 1 0 0 1-1 1A9 9 0 0 1 1 2a1 1 0 0 1 1-1z" fill="#4ba6e6"/></svg>214-555-0187</li>
        <li><svg viewBox="0 0 12 12"><rect x="0.5" y="2" width="11" height="8" fill="#4ba6e6"/><path d="M0.5 2l5.5 4.5L11.5 2" fill="none" stroke="#0d0d0e" stroke-width="1"/></svg>dan@halvorsenguard.com</li>
        <li><svg viewBox="0 0 12 12"><path d="M5 7l2-2M4 5.5L2.5 7a1.8 1.8 0 0 0 2.5 2.5L6.5 8M8 6.5L9.5 5A1.8 1.8 0 0 0 7 2.5L5.5 4" fill="none" stroke="#4ba6e6" stroke-width="1.4" stroke-linecap="round"/></svg>www.halvorsenguardgroup.com</li>
        <li><svg viewBox="0 0 12 12"><rect x="1" y="1" width="10" height="10" rx="1.5" fill="#4ba6e6"/></svg>www.netprofile.com/in/drhalvorsen</li>
      </ul>
    </div>
  </section>

  <section class="card card--back">
    <div class="brand">
      <span class="brand__dot"></span>
      <span class="brand__name">Halvorsen Guard Group</span>
    </div>
  </section>
</main>
</body>
</html>
```